Book Cover and Logo Design

We want a cover designed for a book titled, "The Open Harvest Blueprint" Subtitled "The Decade Program to Rebuild Society, Dissolve the Levy Maze, Clear the Public Ledger, and Revive the Shared Promise" and a logo that we can use on social media when talking about The Open Harvest Blueprint.

This book succeeds Mending Horizon, on the website https://www.mendinghorizon.example

You can see The Open Harvest Blueprint on the website. It gives American's basic income, free healthcare, and free college while slashing personal income taxes and paying off the national debt. The Tide Levy that would replace income taxes would also fund huge infrastructure projects like high speed mag lev trains criss-crossing the nation, a moon base, major desalinization projects to provide water for Western cities and farms.

Target Market(s)

American voters

Industry/Entity Type

American economic policy

Requirements
Must have
• the book cover should be exciting, portraying images of a futuristic America, but with nature tucked into the scenes too
Nice to have
• Patriotic colors
Should not have
• Nothing partisan at all

```html
<!DOCTYPE html>
<html lang="en">
<head>
<meta charset="utf-8">
<title>The Open Harvest Blueprint — Cover and Logo</title>
<link href="https://fonts.googleapis.com/css2?family=Montserrat:wght@600;700;800&family=Oswald:wght@500&display=swap" rel="stylesheet">
<style>
  :root {
    --page-bg: #f4f4f4;
    --cover-black: #0b0b0b;
    --ink-white: #f5f5f5;
    --gold: #cfa43a;
    --gold-deep: #a97f22;
    --label-grey: #d8d8d8;
  }
  * { box-sizing: border-box; margin: 0; padding: 0; }
  html, body { width: 1200px; height: 900px; overflow: hidden; background: var(--page-bg); }
  body { position: relative; font-family: "Montserrat", Arial, sans-serif; }

  .book-cover {
    position: absolute; left: 268px; top: 140px; width: 344px; height: 596px;
    background: var(--cover-black); overflow: hidden; color: var(--ink-white);
  }
  .cover-emblem {
    position: absolute; left: 50%; top: 36px; width: 62px; height: 62px;
    margin-left: -31px; border: 3px solid var(--gold); border-radius: 50%;
  }
  .title-block { position: absolute; left: 0; right: 0; top: 118px; text-align: center; }
  .title-rule-row { display: flex; align-items: center; justify-content: center; gap: 10px; padding: 0 28px; }
  .title-rule { flex: 1; height: 1.5px; background: var(--gold); }
  .title-the { font-weight: 700; font-size: 19px; letter-spacing: 4px; }
  .title-main { font-weight: 800; font-size: 44px; line-height: 1.02; letter-spacing: 1px; }
  .title-gold { color: var(--gold); }
  .title-last { font-weight: 700; font-size: 24px; letter-spacing: 6px; }
  .title-star { display: block; margin: 10px auto 0; }

  .skyline-scene {
    position: absolute; left: 0; right: 0; top: 300px; height: 260px;
    background: linear-gradient(180deg, rgba(11,11,11,1) 0%, #3a3a3a 40%, #6b6b6b 62%, #2a2a2a 75%, #0b0b0b 100%);
  }
  .subtitle {
    position: absolute; left: 0; right: 0; top: 300px; text-align: center;
    font-weight: 600; font-size: 10px; letter-spacing: 1.6px; line-height: 15px; text-transform: uppercase;
  }
  .subtitle .highlight { color: var(--gold); font-weight: 700; }

  .pillar-row {
    position: absolute; left: 38px; right: 18px; top: 520px;
    display: flex; justify-content: space-between;
  }
  .pillar { width: 60px; text-align: center; }
  .pillar svg { display: block; margin: 0 auto 6px; }
  .pillar-label {
    font-family: "Oswald", Arial, sans-serif; font-weight: 500; font-size: 7.5px;
    line-height: 10px; color: var(--label-grey); text-transform: uppercase; letter-spacing: .3px;
  }

  .social-logo {
    position: absolute; left: 748px; top: 432px; width: 254px; height: 108px;
    background: var(--cover-black); display: flex; align-items: center; gap: 14px; padding: 0 18px;
  }
  .social-logo-square { width: 14px; height: 14px; background: var(--gold); flex: none; }
  .social-logo-name {
    font-weight: 700; font-size: 19px; line-height: 1.15; color: var(--gold); text-transform: uppercase;
  }
</style>
</head>
<body>
  <section class="book-cover" aria-label="Book cover">
    <div class="cover-emblem"></div>

    <div class="title-block">
      <div class="title-rule-row"><span class="title-rule"></span><span class="title-the">THE</span><span class="title-rule"></span></div>
      <div class="title-main">OPEN</div>
      <div class="title-main title-gold">HARVEST</div>
      <div class="title-rule-row"><span class="title-rule"></span><span class="title-last">BLUEPRINT</span><span class="title-rule"></span></div>
      <svg class="title-star" width="14" height="14" viewBox="0 0 24 24"><path fill="#a97f22" d="M12 1l3.2 7.2 7.8.7-5.9 5.2 1.8 7.7L12 17.8 5.1 21.8l1.8-7.7L1 8.9l7.8-.7z"/></svg>
    </div>

    <div class="skyline-scene" role="img" aria-label="Night skyline of a futuristic city with a bridge over water and greenery"></div>

    <p class="subtitle">
      The decade program to<br>
      <span class="highlight">Rebuild Society,</span><br>
      Dissolve the levy maze,<br>
      Clear the public ledger,<br>
      and revive<br>
      the shared promise
    </p>

    <div class="pillar-row">
      <div class="pillar">
        <svg width="24" height="26" viewBox="0 0 24 26"><g fill="#cfa43a"><rect x="1" y="18" width="4" height="7"/><rect x="7" y="14" width="4" height="11"/><rect x="13" y="10" width="4" height="15"/><rect x="19" y="6" width="4" height="19"/></g><path d="M1 13 L10 7 L14 9 L22 2" stroke="#cfa43a" stroke-width="1.6" fill="none"/></svg>
        <div class="pillar-label">Rebuild<br>Society</div>
      </div>
      <div class="pillar">
        <svg width="24" height="26" viewBox="0 0 24 26" fill="none" stroke="#cfa43a" stroke-width="1.8"><circle cx="6" cy="20" r="3.5"/><circle cx="18" cy="20" r="3.5"/><path d="M8 17 L19 2 M16 17 L5 2"/></svg>
        <div class="pillar-label">Dissolve<br>the Levy Maze</div>
      </div>
      <div class="pillar">
        <svg width="24" height="26" viewBox="0 0 24 26" fill="#cfa43a"><path d="M12 2 L23 8 H1 Z"/><rect x="3" y="10" width="2.5" height="10"/><rect x="8" y="10" width="2.5" height="10"/><rect x="13.5" y="10" width="2.5" height="10"/><rect x="18.5" y="10" width="2.5" height="10"/><rect x="1" y="21" width="22" height="3"/></svg>
        <div class="pillar-label">Clear the<br>Public Ledger</div>
      </div>
      <div class="pillar">
        <svg width="24" height="26" viewBox="0 0 24 26" fill="none" stroke="#cfa43a" stroke-width="1.8"><circle cx="12" cy="13" r="10"/><path d="M7 13 L11 17 L17 9"/></svg>
        <div class="pillar-label">Revive the<br>Shared Promise</div>
      </div>
      <div class="pillar">
        <svg width="26" height="26" viewBox="0 0 24 24"><path fill="#cfa43a" d="M12 1l3.2 7.2 7.8.7-5.9 5.2 1.8 7.7L12 17.8 5.1 21.8l1.8-7.7L1 8.9l7.8-.7z"/></svg>
        <div class="pillar-label">Secure Our<br>Future</div>
      </div>
    </div>
  </section>

  <section class="social-logo" aria-label="Social media logo">
    <span class="social-logo-square"></span>
    <span class="social-logo-name">The Open Harvest<br>Blueprint</span>
  </section>
</body>
</html>
```